Tarvel Works - Powerpoint Templates

We are a consultancy to help builders to optimize their planning in order to save building costs. For that reason we need templates for teasers and presentations where we offer our services, show our team and their capacities and present workflows, organization charts, price lists etc.

```html
<!DOCTYPE html>
<html lang="en">
<head>
<meta charset="utf-8">
<title>Tarvel Works – Presentation Template</title>
<link href="https://fonts.googleapis.com/css2?family=Audiowide&family=Lato:wght@400;700&display=swap" rel="stylesheet">
<style>
:root{
  --gold:#c3893a;
  --gold-light:#ecc467;
  --dark:#3d3e45;
  --ink:#2e2f35;
  --text:#3a3a3a;
  --page:#1f1f1f;
  --slide-bg:linear-gradient(135deg,#f2f2f2 0%,#ffffff 45%,#ebebeb 100%);
}
*{margin:0;padding:0;box-sizing:border-box}
html,body{width:1200px;height:4121px;overflow:hidden;background:var(--page)}
body{position:relative;font-family:'Lato',sans-serif;color:var(--text)}
.slide{position:absolute;left:46px;width:1096px;height:616px;background:var(--slide-bg);overflow:hidden}
.abs{position:absolute}
.display{font-family:'Audiowide',sans-serif;letter-spacing:2px;text-transform:uppercase}
.heading{position:absolute;left:53px;font-family:'Audiowide',sans-serif;font-size:27px;font-weight:400;letter-spacing:3px;text-transform:uppercase;color:var(--ink)}
.gold{color:var(--gold)}
.top-band{position:absolute;left:0;top:0;width:1040px;height:32px}
.bullets{list-style:none;position:absolute;font-size:17px;line-height:34px}
.bullets li{position:relative;padding-left:26px;margin-bottom:10px}
.bullets li::before{content:"";position:absolute;left:2px;top:12px;width:12px;height:10px;background:var(--gold);clip-path:polygon(0 35%,55% 35%,55% 0,100% 50%,55% 100%,55% 65%,0 65%)}
/* footer */
.footer-brand{position:absolute;left:59px;top:560px;display:flex;align-items:center;gap:10px}
.brand-square{width:26px;height:26px;border:3px solid var(--gold)}
.footer-brand .name{font-family:'Audiowide',sans-serif;font-size:22px;color:var(--ink);letter-spacing:1px;line-height:1}
.footer-brand .tag{font-family:'Audiowide',sans-serif;font-size:10px;color:var(--gold);letter-spacing:3px;margin-top:3px;text-transform:uppercase}
.contact-chip{position:absolute;top:574px;display:flex;align-items:center;gap:8px;font-size:15px;color:var(--ink);white-space:nowrap}
.chip-icon{width:30px;height:30px;border-radius:50%;background:var(--dark);display:flex;align-items:center;justify-content:center}
.page-band{position:absolute;right:0;bottom:0;width:200px;height:31px}
.page-num{position:absolute;right:55px;bottom:4px;font-family:'Audiowide',sans-serif;font-size:16px;color:var(--ink)}
.photo{position:absolute}
/* services */
.house{position:absolute;clip-path:polygon(50% 0,100% 23%,100% 100%,0 100%,0 23%);text-align:center;color:#fff}
.house h3{font-family:'Audiowide',sans-serif;font-size:15px;letter-spacing:1.5px;text-transform:uppercase;font-weight:400}
.house p{font-size:11.5px;line-height:24px;margin:10px auto 0;width:235px}
.house .icon-slot{width:56px;height:56px;margin:0 auto 22px;border:3px solid #fff;border-radius:50%}
/* team */
.frame{position:absolute;clip-path:polygon(50% 0,100% 24%,100% 100%,0 100%,0 24%);padding:9px}
.frame .photo-fill{width:100%;height:100%;clip-path:polygon(50% 0,100% 24%,100% 100%,0 100%,0 24%)}
.member-name{position:absolute;width:269px;text-align:center;font-family:'Audiowide',sans-serif;font-size:21px;letter-spacing:2px;text-transform:uppercase;color:var(--ink)}
.member-role{position:absolute;width:269px;text-align:center;font-size:13px;text-transform:uppercase;color:var(--ink)}
/* contact */
.contact-row{position:absolute;left:53px;display:flex;gap:14px}
.contact-row .pin{width:34px;height:34px;border-radius:50%;background:var(--dark);display:flex;align-items:center;justify-content:center;margin-top:8px}
.contact-row .label{font-family:'Audiowide',sans-serif;font-size:15px;color:var(--ink);letter-spacing:1px;text-transform:uppercase}
.contact-row .value{font-size:19px;color:var(--ink);margin-top:6px}
</style>
</head>
<body>
<svg width="0" height="0" style="position:absolute">
  <defs>
    <linearGradient id="gb" x1="0" x2="1"><stop offset="0" stop-color="#b97e2e"/><stop offset=".6" stop-color="#e9c262"/><stop offset="1" stop-color="#c3893a"/></linearGradient>
    <linearGradient id="db" x1="0" x2="1"><stop offset="0" stop-color="#f1f1f1"/><stop offset=".5" stop-color="#a0a0a4"/><stop offset="1" stop-color="#3d3e45"/></linearGradient>
    <linearGradient id="g1" x1="0" y1="0" x2="1" y2="1"><stop offset="0" stop-color="#b97e2e"/><stop offset="1" stop-color="#ecc467"/></linearGradient>
  </defs>
</svg>

<!-- Slide 1: Welcome -->
<section class="slide" style="top:48px">
  <svg class="abs" style="left:0;top:0" width="1096" height="616"><polygon points="931,88 1096,208 1096,616 931,616" fill="url(#g1)"/></svg>
  <div class="abs" style="left:0;width:1096px;top:150px;display:flex;justify-content:center;align-items:center;gap:16px">
    <div style="width:56px;height:56px;border:5px solid var(--gold)"></div>
    <div class="display" style="font-size:40px;color:var(--gold)">Tarvel Works</div>
  </div>
  <div class="abs display gold" style="left:0;width:1096px;top:365px;text-align:center;font-size:30px;letter-spacing:4px">Welcome to</div>
  <div class="abs display" style="left:0;width:1096px;top:415px;text-align:center;font-size:56px;color:var(--ink);letter-spacing:5px">Tarvel Works</div>
  <div class="abs display" style="left:0;width:1096px;top:494px;text-align:center;font-size:15px;color:var(--ink);letter-spacing:4px">Plan smart, build lean</div>
  <div class="abs" style="left:455px;top:537px;display:flex;gap:15px">
    <span style="width:35px;height:35px;border:3px solid var(--gold);border-radius:50%"></span>
    <span style="width:35px;height:35px;border:3px solid var(--gold);border-radius:50%"></span>
    <span style="width:35px;height:35px;border:3px solid var(--gold);border-radius:50%"></span>
    <span style="width:35px;height:35px;border:3px solid var(--gold);border-radius:50%"></span>
  </div>
</section>

<!-- Slide 2: About -->
<section class="slide" style="top:717px">
  <svg class="top-band" viewBox="0 0 1040 32"><polygon points="0,0 1040,0 1000,32 0,32" fill="url(#gb)"/></svg>
  <h2 class="heading" style="top:52px"><span class="gold">About Tarvel Works</span></h2>
  <ul class="bullets" style="left:53px;top:108px;width:540px">
    <li>Temporibus autem quibusdam et aut officiis debitis aut rerum saepe eveniet ut et voluptaluta recusandae.</li>
    <li>Nam libero tempore, cum soluta nobis est eligendi optio c impedit quo minus id quod maxime placeat facere possimus, voluptas assumenda est, omnis dolor repellendus.</li>
    <li>At vero eos et accusamus et iusto odio dignissimos ducimus qui blanditiis praesentium voluptatum deleniti atque corrupti quos dolores et quas molestias excepturi.</li>
    <li>Itaque earum rerum hic tenetur a sapiente delectus, ut aut reiciendis voluptatibus maiores alias consequatur aut perf erendis doloribus asperiores repellat.</li>
  </ul>
  <svg class="abs" style="left:630px;top:70px" width="440" height="440"><polygon points="28,0 400,40 380,420 8,400" fill="var(--gold)"/><polygon points="10,60 380,70 370,430 0,420" fill="var(--dark)"/></svg>
  <div class="photo" role="img" aria-label="Photo of two consultants meeting at a glass table in a bright office" style="left:658px;top:91px;width:380px;height:389px;background:linear-gradient(135deg,#d9dde0,#9aa2a6 60%,#6d7478)"></div>
  <div class="footer-brand"><div class="brand-square"></div><div><div class="name">TARVEL WORKS</div><div class="tag">Plan smart, build lean</div></div></div>
  <div class="contact-chip" style="left:490px"><span class="chip-icon"><svg width="14" height="10"><rect x="0.5" y="0.5" width="13" height="9" fill="none" stroke="#fff"/><polyline points="0.5,0.5 7,6 13.5,0.5" fill="none" stroke="#fff"/></svg></span>info@tarvelworks.com</div>
  <div class="contact-chip" style="left:718px"><span class="chip-icon"><svg width="14" height="14" viewBox="0 0 24 24"><path d="M6.6 10.8a15 15 0 0 0 6.6 6.6l2.2-2.2c.3-.3.7-.4 1-.2 1.1.4 2.3.6 3.6.6.6 0 1 .4 1 1V20c0 .6-.4 1-1 1A17 17 0 0 1 3 4c0-.6.4-1 1-1h3.5c.6 0 1 .4 1 1 0 1.3.2 2.5.6 3.6.1.3 0 .7-.2 1z" fill="#fff"/></svg></span>+1 555 014 2290</div>
  <svg class="page-band" viewBox="0 0 200 31"><polygon points="30,0 200,0 200,31 0,31" fill="url(#gb)"/></svg>
  <div class="page-num">02</div>
</section>

<!-- Slide 3: Services -->
<section class="slide" style="top:1384px">
  <svg class="top-band" viewBox="0 0 1040 32"><polygon points="0,0 1040,0 1000,32 0,32" fill="url(#db)"/></svg>
  <h2 class="heading" style="top:52px">We Offer <span class="gold">Our</span> Services</h2>
  <p class="abs" style="left:53px;top:100px;width:1000px;font-size:17px;line-height:34px">Temporibus autem quibusdam et aut officiis debitis aut rerum necessitatibus saepe eveniet ut et voluptates repudiandae sint et molestiae non recusandae.</p>
  <div class="house" style="left:53px;top:197px;width:269px;height:254px;background:var(--dark);padding-top:52px">
    <div class="icon-slot"></div>
    <h3>Temporibus Autem</h3>
    <p>Temporibus autem quibusdam et aut officiis debitis aut rerum necessitatibus saepe eveniet ut et voluptates</p>
  </div>
  <div class="house" style="left:414px;top:248px;width:268px;height:256px;background:var(--gold);padding-top:52px">
    <div class="icon-slot"></div>
    <h3>Itaque Earum Rerum</h3>
    <p>Itaque earum rerum hic tenetur a sapiente delectus, ut aut reiciendis voluptatibus maiores alias consequatur</p>
  </div>
  <div class="house" style="left:773px;top:197px;width:269px;height:254px;background:var(--dark);padding-top:52px">
    <div class="icon-slot"></div>
    <h3>Nam Libero Tempore</h3>
    <p>Nam libero tempore, cum soluta nobis est eligendi optio cumque nihil impedit quo minus id quod maxime placeat</p>
  </div>
  <div class="footer-brand"><div class="brand-square"></div><div><div class="name">TARVEL WORKS</div><div class="tag">Plan smart, build lean</div></div></div>
  <div class="contact-chip" style="left:490px"><span class="chip-icon"><svg width="14" height="10"><rect x="0.5" y="0.5" width="13" height="9" fill="none" stroke="#fff"/><polyline points="0.5,0.5 7,6 13.5,0.5" fill="none" stroke="#fff"/></svg></span>info@tarvelworks.com</div>
  <div class="contact-chip" style="left:718px"><span class="chip-icon"><svg width="14" height="14" viewBox="0 0 24 24"><path d="M6.6 10.8a15 15 0 0 0 6.6 6.6l2.2-2.2c.3-.3.7-.4 1-.2 1.1.4 2.3.6 3.6.6.6 0 1 .4 1 1V20c0 .6-.4 1-1 1A17 17 0 0 1 3 4c0-.6.4-1 1-1h3.5c.6 0 1 .4 1 1 0 1.3.2 2.5.6 3.6.1.3 0 .7-.2 1z" fill="#fff"/></svg></span>+1 555 014 2290</div>
  <svg class="page-band" viewBox="0 0 200 31"><polygon points="30,0 200,0 200,31 0,31" fill="url(#db)"/></svg>
  <div class="page-num" style="color:#fff">03</div>
</section>

<!-- Slide 4: Organization chart -->
<section class="slide" style="top:2064px">
  <svg class="top-band" viewBox="0 0 1040 32"><polygon points="0,0 1040,0 1000,32 0,32" fill="url(#gb)"/></svg>
  <h2 class="heading" style="top:50px"><span class="gold">Organization Charts</span></h2>
  <svg class="abs" style="left:40px;top:115px" width="600" height="400" font-family="Arial, sans-serif" font-size="11" fill="#333">
    <g stroke="#e3e3e3">
      <line x1="40" y1="16" x2="580" y2="16"/><line x1="40" y1="69" x2="580" y2="69"/><line x1="40" y1="127" x2="580" y2="127"/><line x1="40" y1="184" x2="580" y2="184"/><line x1="40" y1="242" x2="580" y2="242"/><line x1="40" y1="294" x2="580" y2="294"/><line x1="40" y1="349" x2="580" y2="349"/>
    </g>
    <g text-anchor="end"><text x="30" y="20">120</text><text x="30" y="73">100</text><text x="30" y="131">80</text><text x="30" y="188">60</text><text x="30" y="246">40</text><text x="30" y="298">20</text><text x="30" y="353">0</text></g>
    <g font-weight="bold" text-anchor="middle">
      <text x="83" y="371">Sun</text><text x="160" y="371">Mon</text><text x="235" y="371">Tue</text><text x="312" y="371">Wed</text><text x="387" y="371">Thu</text><text x="459" y="371">Fri</text><text x="533" y="371">Sat</text>
    </g>
    <g fill="#c3893a">
      <rect x="64" y="72" width="13" height="277"/><rect x="141" y="99" width="13" height="250"/><rect x="216" y="210" width="13" height="139"/><rect x="293" y="72" width="13" height="277"/><rect x="368" y="72" width="13" height="277"/><rect x="440" y="183" width="13" height="166"/><rect x="514" y="210" width="13" height="139"/>
    </g>
    <g fill="#3d3e45">
      <rect x="88" y="99" width="13" height="250"/><rect x="165" y="127" width="13" height="222"/><rect x="240" y="72" width="13" height="277"/><rect x="317" y="183" width="13" height="166"/><rect x="392" y="99" width="13" height="250"/><rect x="464" y="141" width="13" height="208"/><rect x="538" y="72" width="13" height="277"/>
    </g>
    <g text-anchor="middle">
      <text x="70" y="64">100</text><text x="95" y="91">90</text><text x="147" y="91">90</text><text x="172" y="119">80</text><text x="222" y="202">50</text><text x="246" y="64">100</text><text x="299" y="64">100</text><text x="323" y="175">60</text><text x="374" y="64">100</text><text x="398" y="91">90</text><text x="446" y="175">60</text><text x="470" y="133">75</text><text x="520" y="202">50</text><text x="544" y="64">100</text>
    </g>
  </svg>
  <ul class="bullets" style="left:658px;top:112px;width:400px">
    <li>Temporibus autem quibusdam et aut officiis debitis aut rerum necessitatibus saepe eveniet ut et voluptates repudiandae sint et molestiae non tempore, cum soluta recusandae.</li>
    <li>Nam libero tempore, cum soluta nobis est eligendi optio cumque nihil impedit quo min us id quod maxime.</li>
    <li>Itaque earum rerum hic tenetur a sapiente delectus, ut aut reiciendis voluptatibus doloribus asperiores repellat.</li>
  </ul>
  <div class="footer-brand"><div class="brand-square"></div><div><div class="name">TARVEL WORKS</div><div class="tag">Plan smart, build lean</div></div></div>
  <div class="contact-chip" style="left:490px"><span class="chip-icon"><svg width="14" height="10"><rect x="0.5" y="0.5" width="13" height="9" fill="none" stroke="#fff"/><polyline points="0.5,0.5 7,6 13.5,0.5" fill="none" stroke="#fff"/></svg></span>info@tarvelworks.com</div>
  <div class="contact-chip" style="left:718px"><span class="chip-icon"><svg width="14" height="14" viewBox="0 0 24 24"><path d="M6.6 10.8a15 15 0 0 0 6.6 6.6l2.2-2.2c.3-.3.7-.4 1-.2 1.1.4 2.3.6 3.6.6.6 0 1 .4 1 1V20c0 .6-.4 1-1 1A17 17 0 0 1 3 4c0-.6.4-1 1-1h3.5c.6 0 1 .4 1 1 0 1.3.2 2.5.6 3.6.1.3 0 .7-.2 1z" fill="#fff"/></svg></span>+1 555 014 2290</div>
  <svg class="page-band" viewBox="0 0 200 31"><polygon points="30,0 200,0 200,31 0,31" fill="url(#gb)"/></svg>
  <div class="page-num">04</div>
</section>

<!-- Slide 5: Team -->
<section class="slide" style="top:2739px">
  <svg class="top-band" viewBox="0 0 1040 32"><polygon points="0,0 1040,0 1000,32 0,32" fill="url(#db)"/></svg>
  <h2 class="heading" style="top:52px">Our <span class="gold">Team</span></h2>
  <div class="frame" style="left:53px;top:109px;width:269px;height:256px;background:var(--dark)"><div class="photo-fill" role="img" aria-label="Portrait of team member in a dark suit" style="background:linear-gradient(180deg,#c9ced3,#8f979d)"></div></div>
  <div class="member-name" style="left:53px;top:384px">John Doe</div>
  <div class="member-role" style="left:53px;top:421px">Temporibus</div>
  <div class="frame" style="left:414px;top:154px;width:268px;height:258px;background:var(--gold)"><div class="photo-fill" role="img" aria-label="Portrait of team member in a blue shirt" style="background:linear-gradient(180deg,#cfd6dc,#7fa6c4)"></div></div>
  <div class="member-name" style="left:414px;top:430px">Marco Ellis</div>
  <div class="member-role" style="left:414px;top:467px">Itaque Earum</div>
  <div class="frame" style="left:773px;top:109px;width:269px;height:256px;background:var(--dark)"><div class="photo-fill" role="img" aria-label="Portrait of team member in a white blouse" style="background:linear-gradient(180deg,#bcc9d2,#8896a2)"></div></div>
  <div class="member-name" style="left:773px;top:384px">Lena Hartwig</div>
  <div class="member-role" style="left:773px;top:421px">Necessitatibu</div>
  <div class="footer-brand"><div class="brand-square"></div><div><div class="name">TARVEL WORKS</div><div class="tag">Plan smart, build lean</div></div></div>
  <div class="contact-chip" style="left:490px"><span class="chip-icon"><svg width="14" height="10"><rect x="0.5" y="0.5" width="13" height="9" fill="none" stroke="#fff"/><polyline points="0.5,0.5 7,6 13.5,0.5" fill="none" stroke="#fff"/></svg></span>info@tarvelworks.com</div>
  <div class="contact-chip" style="left:718px"><span class="chip-icon"><svg width="14" height="14" viewBox="0 0 24 24"><path d="M6.6 10.8a15 15 0 0 0 6.6 6.6l2.2-2.2c.3-.3.7-.4 1-.2 1.1.4 2.3.6 3.6.6.6 0 1 .4 1 1V20c0 .6-.4 1-1 1A17 17 0 0 1 3 4c0-.6.4-1 1-1h3.5c.6 0 1 .4 1 1 0 1.3.2 2.5.6 3.6.1.3 0 .7-.2 1z" fill="#fff"/></svg></span>+1 555 014 2290</div>
  <svg class="page-band" viewBox="0 0 200 31"><polygon points="30,0 200,0 200,31 0,31" fill="url(#db)"/></svg>
  <div class="page-num" style="color:#fff">05</div>
</section>

<!-- Slide 6: Contact -->
<section class="slide" style="top:3429px">
  <svg class="top-band" viewBox="0 0 1040 32"><polygon points="0,0 1040,0 1000,32 0,32" fill="url(#gb)"/></svg>
  <h2 class="heading" style="top:52px"><span class="gold">Get in Touch with Us</span></h2>
  <div class="contact-row" style="top:118px">
    <span class="pin"><svg width="14" height="18" viewBox="0 0 24 30"><path d="M12 0a10 10 0 0 0-10 10c0 8 10 20 10 20s10-12 10-20A10 10 0 0 0 12 0zm0 14a4 4 0 1 1 0-8 4 4 0 0 1 0 8z" fill="#fff"/></svg></span>
    <div><div class="label">Address:</div><div class="value">Tarvel Works, United States</div></div>
  </div>
  <div class="contact-row" style="top:215px">
    <span class="pin"><svg width="14" height="10"><rect x="0.5" y="0.5" width="13" height="9" fill="none" stroke="#fff"/><polyline points="0.5,0.5 7,6 13.5,0.5" fill="none" stroke="#fff"/></svg></span>
    <div><div class="label">Email Us:</div><div class="value">info@tarvelworks.com</div></div>
  </div>
  <div class="contact-row" style="top:316px">
    <span class="pin"><svg width="14" height="14" viewBox="0 0 24 24"><path d="M6.6 10.8a15 15 0 0 0 6.6 6.6l2.2-2.2c.3-.3.7-.4 1-.2 1.1.4 2.3.6 3.6.6.6 0 1 .4 1 1V20c0 .6-.4 1-1 1A17 17 0 0 1 3 4c0-.6.4-1 1-1h3.5c.6 0 1 .4 1 1 0 1.3.2 2.5.6 3.6.1.3 0 .7-.2 1z" fill="#fff"/></svg></span>
    <div><div class="label">Phone Number:</div><div class="value">+1 555 014 2290</div></div>
  </div>
  <div class="abs display" style="left:53px;top:430px;font-size:40px;color:var(--ink);letter-spacing:4px">Thank You</div>
  <div class="abs display" style="left:53px;top:498px;font-size:40px;color:var(--ink);letter-spacing:4px">Tarvel Works</div>
  <div class="abs" style="left:670px;top:230px;width:380px;display:flex;flex-direction:column;align-items:center;gap:24px">
    <div style="width:110px;height:110px;border:8px solid var(--gold)"></div>
    <div class="display" style="font-size:34px;color:var(--gold)">Tarvel Works</div>
  </div>
  <svg class="page-band" viewBox="0 0 200 31"><polygon points="30,0 200,0 200,31 0,31" fill="url(#gb)"/></svg>
  <div class="page-num">06</div>
</section>

</body>
</html>
```